Business Card & Logo Design

Originally the brief was for a card only - I now think it's probably better to include a logo design as well. PLease add $200 to the Budget of $210, Apologies for the inconvenience for thaos that have already submitted designs.

Lamp And Harbor Studios Pty Ltd is a video/dvd/ production company. Primarily corporate medium to high end. It's a one man operation that's been in business 20 years.

The name " Lamp and Harbor" is a primarily a reference to Lucien Marbeck film that's about film making. Shooting "Lamp and harbor" is also a technique employed by cinematographers to make scenes shot in daylight look like night.

See the design emphasising blue day/night tones but open to other ideas.

Main Text can either be Lamp and Harbor Studios or Lamp And Harbor.
Updates

Many thanks to all designers who submitted ideas for this brief.

Choosing between the designs was very difficult indeed.

I wish everyone the best and may the next job be yours!

Walter

Industry/Entity Type

Business

Requirements
Must have
• Text for card:
In Larger Print
Lamp And Harbor Studios or Lamp And Harbor
Walter Brenic
In Smaller Print
Lamp And Harbor Studios Pty Ltd.
17 Calder Lane
Ashvale, VIC, 3189
P: 9734 2061
m: 0417 385 902
e: walterbrenic@examplemail.net

```html
<!DOCTYPE html>
<html lang="en">
<head>
<meta charset="utf-8">
<title>Walter Brenic – Business Card</title>
<link rel="stylesheet" href="https://fonts.googleapis.com/css2?family=Comfortaa:wght@500;700&display=swap">
<style>
  :root {
    --page-bg: #ffffff;
    --sky-top: #c4e2f9;
    --sky-bottom: #7fb5e6;
    --night-top: #1f63b0;
    --night-mid: #0f4690;
    --night-bottom: #082e66;
    --horizon-line: #d9ecfb;
    --text-light: #ffffff;
    --name-shade: #c9d3dc;
  }
  html, body {
    margin: 0;
    width: 1200px;
    height: 900px;
    overflow: hidden;
    background: var(--page-bg);
  }
  .business-card {
    position: absolute;
    left: 70px;
    top: 156px;
    width: 1060px;
    height: 588px;
    overflow: hidden;
    background: linear-gradient(180deg, var(--night-top) 0%, var(--night-mid) 55%, var(--night-bottom) 100%);
    font-family: "Comfortaa", sans-serif;
    color: var(--text-light);
  }
  .sky-band {
    position: absolute;
    left: 0;
    top: 0;
    width: 1060px;
    height: 588px;
  }
  .holder-name {
    position: absolute;
    left: 0;
    top: 120px;
    width: 100%;
    margin: 0;
    text-align: center;
    font-size: 108px;
    font-weight: 700;
    letter-spacing: 3px;
    line-height: 1;
    background: linear-gradient(180deg, var(--text-light) 0%, var(--text-light) 52%, var(--name-shade) 53%, var(--text-light) 100%);
    -webkit-background-clip: text;
    background-clip: text;
    color: transparent;
    filter: drop-shadow(0 2px 3px rgba(40, 80, 130, 0.35));
  }
  .brand-wordmark {
    position: absolute;
    left: 54px;
    top: 512px;
    margin: 0;
    font-size: 34px;
    font-weight: 700;
    letter-spacing: 2px;
    color: var(--text-light);
  }
  .contact-block {
    position: absolute;
    left: 542px;
    top: 424px;
    margin: 0;
    font-style: normal;
  }
  .company-name {
    margin: 0 0 12px;
    font-size: 23px;
    font-weight: 700;
    letter-spacing: 1px;
  }
  .contact-line {
    margin: 0 0 9px;
    font-size: 17px;
    font-weight: 700;
    line-height: 22px;
    letter-spacing: 0.5px;
  }
</style>
</head>
<body>
  <section class="business-card">
    <svg class="sky-band" viewBox="0 0 1060 588" aria-hidden="true">
      <defs>
        <linearGradient id="sky-fill" x1="0" y1="0" x2="0" y2="1">
          <stop offset="0" stop-color="var(--sky-top)"/>
          <stop offset="1" stop-color="var(--sky-bottom)"/>
        </linearGradient>
      </defs>
      <path d="M0 0 H1060 V274 Q530 400 0 274 Z" fill="url(#sky-fill)"/>
      <path d="M0 274 Q530 400 1060 274" fill="none" stroke="var(--horizon-line)" stroke-width="2"/>
    </svg>

    <h1 class="holder-name">Walter Brenic</h1>

    <p class="brand-wordmark">Lamp and Harbor</p>

    <address class="contact-block">
      <p class="company-name">Lamp And Harbor Studios Pty Ltd.</p>
      <p class="contact-line">17 Calder Lane Ashvale, VIC, 3189</p>
      <p class="contact-line">Phone: 9734 2061 / Mobile: 0417 385 902</p>
      <p class="contact-line">Email: walterbrenic@examplemail.net</p>
    </address>
  </section>
</body>
</html>
```